PLUM BUSINESS CARD

Need a business card and logo. The company name is PLUM (Coastal Society of Junior Equestrian Arts). It's a business that offers horseback riding lessons to young girls. Please put my name: Marlene Tobbitt and a place for email and phone number. I would like the card to look feminine and soft. I like script type lettering. I want the card to be white or ivory with black or gray and hot pink print. A horse head outline would be cool, something whimsical. Think teen girl who likes glamour. Also, I give western riding lessons. So I like faded out background Images of western saddles, cowgirls, horses with long hair, ropes, horses in sunset...mabe the word PLUM can be made out of a lasso rope?

Just updated my project with a little more detail

Target Market(s)

Young girls/ cowgirls, western riding

Industry/Entity Type

Horseback Riding

Font styles to use
Script

Colors
e34197

Requirements
Must have
• A logo of PLUM.
Must say Coastal Society of Junior Equestrian Arts
Colors are Pink and Black with an elegant, glamorous, feminine look.
Nice to have
• Could have a picture or outline of a horse

```html
<!DOCTYPE html>
<html lang="en">
<head>
<meta charset="utf-8">
<title>PLUM Business Card</title>
<link href="https://fonts.googleapis.com/css2?family=Arimo&family=Great+Vibes&display=swap" rel="stylesheet">
<style>
  :root {
    --page: #ffffff;
    --card: #ffffff;
    --ink: #111111;
    --pink: #ef1fe8;
    --rope-pink: #c44bd0;
  }
  html, body {
    margin: 0;
    padding: 0;
    width: 1200px;
    height: 1190px;
    overflow: hidden;
    background: var(--page);
  }
  .card {
    position: absolute;
    left: 326px;
    top: 450px;
    width: 542px;
    height: 308px;
    background: var(--card);
    border: 2px solid var(--ink);
    box-sizing: border-box;
    overflow: hidden;
  }
  .card-base {
    position: absolute;
    inset: 0;
    width: 100%;
    height: 100%;
  }
  .brand-name {
    position: absolute;
    left: 12px;
    top: 25px;
    margin: 0;
    font-family: "Arimo", Arial, sans-serif;
    font-weight: 400;
    font-size: 134px;
    line-height: 134px;
    letter-spacing: 0;
    color: var(--rope-pink);
    white-space: nowrap;
  }
  .rider-art {
    position: absolute;
    left: 392px;
    top: 35px;
    width: 134px;
    height: 114px;
    border-radius: 38%;
    background: linear-gradient(160deg, #2a2a2a 0%, #111111 100%);
  }
  .tagline {
    position: absolute;
    left: 33px;
    top: 151px;
    margin: 0;
    font-family: "Arimo", Arial, sans-serif;
    font-size: 22px;
    line-height: 24px;
    color: var(--ink);
    white-space: nowrap;
  }
  .holder-name {
    position: absolute;
    left: 34px;
    top: 244px;
    margin: 0;
    font-family: "Great Vibes", cursive;
    font-size: 36px;
    line-height: 1;
    color: var(--ink);
    white-space: nowrap;
  }
  .contact {
    position: absolute;
    left: 354px;
    top: 244px;
    font-family: "Great Vibes", cursive;
    color: var(--ink);
    line-height: 1;
    white-space: nowrap;
  }
  .contact-phone { font-size: 24px; letter-spacing: 1px; }
  .contact-email { font-size: 17px; margin-top: 12px; }
</style>
</head>
<body>
  <div class="card">
    <svg class="card-base" viewBox="0 0 542 308" preserveAspectRatio="none" aria-hidden="true">
      <path d="M0 220 C 180 196, 380 192, 542 202 L542 308 L0 308 Z" fill="var(--pink)"/>
      <path d="M0 220 C 180 196, 380 192, 542 202 L542 181 C 380 176, 180 182, 0 210 Z" fill="var(--ink)"/>
    </svg>

    <h1 class="brand-name">PLUM</h1>
    <div class="rider-art" role="img" aria-label="Black silhouette of a rider on a jumping horse"></div>
    <p class="tagline">Coastal Society of Junior Equestrian Arts</p>

    <p class="holder-name">Marlene Tobbitt</p>
    <div class="contact">
      <div class="contact-phone">(222) 222-2222</div>
      <div class="contact-email">email goes here</div>
    </div>
  </div>
</body>
</html>
```